Refresh of a rather uncommon tech outfit website

Our web site is starting to show it's age. You can see the existing site here: www.plumfarrow.net. As a growing company we want to come across as a dynamic collection of IT experts.

We want to update the design so are open to any colour palette and look, but want to retain our current table logo. We use the logo on our business cards but with a white background - see the attached file, so you don't need to keep the brown or the green.

The design should consider the range of browsers that will be looking at the site - so please show how it will look on a wide screen laptop and a 768x1024 tablet.

We want to add some pages about our team and their skills, probably with photos of each person on the team.

This is an uncoded project - the PSD files of the design is required, not coding.
Updates

Thanks everyone for the submissions so far.  It's a holiday day in the UK today but we will get some feedback on the designs so far out to you.

Target Market(s)

Architects and other creative types looking for IT support

Industry/Entity Type

Business

Font styles to use
Serif
Sans Serif

Requirements
Must have
• Must look good on a laptop and an Zelva.

```html
<!DOCTYPE html>
<html lang="en">
<head>
<meta charset="utf-8">
<title>plumfarrow – Serious IT Support for Business</title>
<link rel="stylesheet" href="https://fonts.googleapis.com/css2?family=Yanone+Kaffeesatz:wght@300;400&family=Jost:wght@400;500&family=Arimo&display=swap">
<style>
:root{
  --plum:#8c0b4e;
  --mustard:#d4a90c;
  --slate:#5d6670;
  --ink:#1e1e1e;
  --panel:#e4e5e4;
  --panel-edge:#d6d7d6;
  --green:#5aa628;
  --lime:#8cc21c;
  --footer:#222327;
  --hero-caption:rgba(25,25,25,.82);
}
*{box-sizing:border-box;margin:0;padding:0}
html,body{width:1200px;height:1099px;overflow:hidden;background:#fff}
body{position:relative;font-family:"Arimo",Arial,sans-serif;color:var(--ink)}
.abs{position:absolute}
.head-font{font-family:"Yanone Kaffeesatz","Arial Narrow",sans-serif;font-weight:300}

.brand{left:213px;top:55px;display:flex;align-items:center;gap:80px}
.brand-mark{width:34px;height:34px;background:var(--mustard)}
.brand-name{font-family:"Jost",sans-serif;font-weight:500;font-size:52px;color:var(--plum);letter-spacing:.3px;line-height:1}

.social{top:16px;left:683px;display:flex;gap:9px}
.social span{width:23px;height:23px;display:block}
.contact-line{top:16px;left:789px;font-family:"Yanone Kaffeesatz",sans-serif;font-size:17px;color:var(--plum);display:flex;gap:10px;line-height:23px}
.contact-line .sep{color:var(--slate)}

.main-nav{top:81px;right:205px;display:flex;gap:13px;font-size:20px;color:var(--slate);text-transform:uppercase}

.hero{left:0;top:145px;width:1200px;height:364px;background:linear-gradient(90deg,#c9c8e6 0%,#b9b8dd 15%,#8e96a0 18%,#d8dce0 40%,#a2a8ae 60%,#6ea6e3 68%,#4b8ee6 85%,#3a6fd8 100%)}
.hero-caption{left:188px;top:384px;width:422px;height:115px;background:var(--hero-caption);text-align:center}
.hero-title{font-family:"Yanone Kaffeesatz",sans-serif;font-weight:400;font-size:54px;color:#fff;line-height:1;padding-top:14px}
.hero-sub{font-family:"Yanone Kaffeesatz",sans-serif;font-weight:400;font-size:32px;color:var(--mustard);letter-spacing:1.5px;line-height:1;margin-top:4px}
.slider-dots{left:950px;top:481px;display:flex;gap:6px}
.slider-dots span{width:11px;height:11px;border-radius:50%;background:#7a7670}
.slider-dots span.on{background:#000}

.about-title{left:184px;top:554px;font-size:30px}
.body-copy{font-size:10.3px;line-height:17px;text-align:justify;color:#222}
.about-copy{left:186px;top:597px;width:556px}

.img-cloud{left:173px;top:727px;width:158px;height:135px;background:linear-gradient(135deg,#d8ebfb 0%,#a9cdf0 45%,#3a3f46 75%,#1b1b1b 100%)}
.img-cad{left:463px;top:730px;width:207px;height:128px;background:linear-gradient(135deg,#0a3d9a,#1f6fd0 50%,#6aa8e8 75%,#1a5cc0)}
.service-title{top:866px;font-size:30px}
.service-copy{top:905px}

.sidebar{left:789px;top:550px;width:288px;height:413px;background:var(--panel);border:1px solid var(--panel-edge);border-radius:3px}
.side-title{left:24px;font-size:29px;color:#222}
.side-copy{left:25px;width:250px;font-family:"Jost",sans-serif;font-size:12.3px;line-height:18.5px;color:#2a2a2a}
.session{left:23px;top:294px;width:187px;height:42px;border:2px solid var(--lime);background:#fff;font-family:"Arimo",sans-serif;font-size:14px;color:#999;padding:12px 0 0 14px}
.go{left:23px;top:349px;width:48px;height:34px;background:var(--green);border-radius:3px;color:#fff;font-family:"Jost",sans-serif;font-size:17px;text-align:center;line-height:34px}

.footer{left:0;top:1054px;width:1200px;height:45px;background:var(--footer);border-top:2px solid #000;color:#e6e6e6;font-size:10.5px;text-align:center;line-height:42px}
</style>
</head>
<body>

<header>
  <div class="abs brand">
    <span class="brand-mark"></span>
    <span class="brand-name">plumfarrow</span>
  </div>
  <div class="abs social" aria-label="Social links">
    <span style="background:#3b5998"></span>
    <span style="background:#1da1f2"></span>
    <span style="background:#dd4b39"></span>
  </div>
  <div class="abs contact-line"><span>020 7946 0312</span><span class="sep">|</span><span>website@plumfarrow.net</span></div>
  <nav class="abs main-nav head-font"><span>About</span><span>What we do</span><span>News</span><span>Articles</span><span>Contact</span></nav>
</header>

<section>
  <div class="abs hero" role="img" aria-label="Technician working at a server rack beside a glowing blue cloud and circuit graphic"></div>
  <div class="abs hero-caption">
    <div class="hero-title">SERIOUS IT SUPPORT</div>
    <div class="hero-sub">FOR BUSINESS</div>
  </div>
  <div class="abs slider-dots"><span></span><span></span><span class="on"></span></div>
</section>

<main>
  <h2 class="abs about-title head-font">About plumfarrow</h2>
  <p class="abs body-copy about-copy">Lorem ipsum dolor sit amet, consectetur adipiscing elit. Sed at ante. Mauris eleifend, quam a vulputate dictum, massa quam dapibus leo, eget vulputate orci purus ut lorem. In fringilla mi in ligula. Pellentesque aliquam quam vel dolor. Nunc adipiscing. Sed quam odio, tempus ac, aliquam molestie, varius ac, tellus. Vestibulum ut nulla aliquam risus rutrum interdum. Pellentesque lorem. Curabitur sit amet erat quis risus feugiat viverra. Pellentesque augue justo, sagittis et, lacinia at, venenatis non, arcu. Nunc nec libero. In cursus dictum risus. Etiam tristique nisl a nulla. Ut a orci. Curabitur dolor nunc, egestas at, accumsan at, malesuada nec, magna.</p>

  <div class="abs img-cloud" role="img" aria-label="Cloud computing illustration"></div>
  <h3 class="abs service-title head-font" style="left:173px">Cloud Computing</h3>
  <p class="abs body-copy service-copy" style="left:174px;width:260px">Lorem ipsum dolor sit amet, consectetur adipiscing elit. Sed at ante. Mauris eleifend, quam a vulputate dictum, massa quam dapibus leo, eget vulputate orci purus ut lorem. In fringilla mi in ligula. Pellentesque aliquam quam vel dolor. Nunc adipiscing. Sed quam odio,</p>

  <div class="abs img-cad" role="img" aria-label="Abstract blue 3D rendered knot shape"></div>
  <h3 class="abs service-title head-font" style="left:465px">CAD Services</h3>
  <p class="abs body-copy service-copy" style="left:466px;width:288px">Lorem ipsum dolor sit amet, consectetur adipiscing elit. Sed at ante. Mauris eleifend, quam a vulputate dictum, massa quam dapibus leo, eget vulputate orci purus ut lorem. In fringilla mi in ligula. Pellentesque aliquam quam vel dolor. Nunc adipiscing. Sed quam odio, tempus ac, aliquam molestie, varius ac, tellus.</p>

  <aside class="abs sidebar">
    <h3 class="abs side-title head-font" style="top:18px">Latest News</h3>
    <p class="abs side-copy" style="top:64px">Lorem ipsum dolor sit amet, consectetur adipiscing elit, sed do eiusmod tempor incididunt ut labore et dolore magna aliqua.</p>
    <h3 class="abs side-title head-font" style="top:129px">Latest Articles</h3>
    <p class="abs side-copy" style="top:175px">Lorem ipsum dolor sit amet, consectetur adipiscing elit, sed do eiusmod tempor incididunt ut labore et dolore magna aliqua.</p>
    <h3 class="abs side-title head-font" style="top:247px">Remote</h3>
    <div class="abs session">Session ID</div>
    <div class="abs go">Go</div>
  </aside>
</main>

<footer class="abs footer">Copyright 2014 Plumfarrow - Terms &amp; Conditions | Privacy Policy</footer>

</body>
</html>
```